HALDEN DENTAL *

Target Market(s)

Adults 18-60

Contact Information for Business Card

Website: haldendentalvlm.com
Phone number 555 304 2796 email: crestdentalvlm@mailbox-example.com
Address:471 S. Holloway rd
Suite#24, TX70000
Dr. Marcus Telfer, DDS

Font styles to use
Sans Serif

Requirements
Must have
• Logo, phone number website, doctor,
• 's name

```html
<!DOCTYPE html>
<html lang="en">
<head>
<meta charset="utf-8">
<title>Halden Dental — Business Card</title>
<link rel="stylesheet" href="https://fonts.googleapis.com/css2?family=Lato:wght@400;700&family=Open+Sans:wght@400&display=swap">
<style>
  :root {
    --backdrop: #8a5a32;
    --kraft-light: #dbb58a;
    --kraft-mid: #c89a6b;
    --kraft-dark: #b6865a;
    --ink-navy: #1c2b45;
    --ink-body: #2a2622;
    --ink-black: #161310;
    --rule: #5b4a3a;
  }
  * { margin: 0; padding: 0; box-sizing: border-box; }
  html, body {
    width: 1200px;
    height: 900px;
    overflow: hidden;
    background: var(--backdrop);
  }
  .canvas {
    position: relative;
    width: 1200px;
    height: 900px;
  }
  .card {
    position: absolute;
    width: 556px;
    height: 343px;
    background: linear-gradient(160deg, var(--kraft-light) 0%, var(--kraft-mid) 50%, var(--kraft-dark) 100%);
    box-shadow: 2px 4px 6px rgba(0, 0, 0, 0.35);
  }
  .card-front { left: 330px; top: 91px; }
  .card-back { left: 330px; top: 469px; }

  .doctor-name {
    position: absolute;
    top: 112px;
    width: 100%;
    text-align: center;
    font-family: "Lato", sans-serif;
    font-weight: 700;
    font-size: 21px;
    letter-spacing: 0.3px;
    color: var(--ink-navy);
  }
  .doctor-name .credential {
    font-weight: 400;
    font-size: 15px;
  }
  .divider {
    position: absolute;
    top: 159px;
    left: 220px;
    width: 116px;
    height: 1px;
    background: var(--rule);
  }
  .contact {
    position: absolute;
    top: 180px;
    width: 100%;
    text-align: center;
    font-family: "Open Sans", sans-serif;
    font-size: 17px;
    line-height: 24px;
    color: var(--ink-body);
  }

  .brand-mark {
    position: absolute;
    top: 99px;
    left: 233px;
    width: 90px;
    height: 90px;
  }
  .brand-name {
    position: absolute;
    top: 202px;
    width: 100%;
    text-align: center;
    font-family: "Lato", sans-serif;
    font-weight: 400;
    font-size: 38px;
    line-height: 46px;
    letter-spacing: 1px;
    white-space: nowrap;
    color: var(--ink-black);
  }
</style>
</head>
<body>
<main class="canvas">
  <section class="card card-front">
    <h1 class="doctor-name">DR. MARCUS TELFER<span class="credential">, DDS</span></h1>
    <div class="divider"></div>
    <p class="contact">
      555 304 2796<br>
      www.haldendentalvlm.com
    </p>
  </section>

  <section class="card card-back">
    <svg class="brand-mark" viewBox="0 0 90 90" aria-hidden="true">
      <circle cx="45" cy="45" r="44" fill="none" stroke="#161310" stroke-width="1.6"/>
    </svg>
    <p class="brand-name">HALDEN DENTAL</p>
  </section>
</main>
</body>
</html>
```